Electrician Needs A Business Card

I already have a logo and would like a business card to be designed based around this logo the company is called Coralwood Electrical Pty Ltd

The business card will be printed on transparent plastic so I need it to stand out from the crowd. I do not want the card to have anything to do with Electrical on it eg light bulbs, power points etc

I need it to have the following details.

Dominic Farrow
Mobile : 0452 317 908
email : dominic@coralwoodelectrical.com.au

If it could incorporate the following onto the bottom of the card
ELECTRICAL - COMMUNICATIONS - AUDIO - VISUAL

```html
<!DOCTYPE html>
<html lang="en">
<head>
<meta charset="utf-8">
<title>Coralwood Electrical – Business Card</title>
<link rel="stylesheet" href="https://fonts.googleapis.com/css2?family=Source+Sans+3:wght@400;600&display=swap">
<style>
  :root {
    --backdrop: #d8d5d0;
    --card: #efeeeb;
    --card-edge: #c9c6c1;
    --ink: #1f1f1f;
    --accent: #e0861f;
    --accent-deep: #c96f12;
  }
  * { margin: 0; padding: 0; box-sizing: border-box; }
  html, body {
    width: 1200px;
    height: 970px;
    overflow: hidden;
    background: var(--backdrop);
    font-family: "Source Sans 3", "Source Sans Pro", sans-serif;
    color: var(--ink);
  }
  .card {
    position: absolute;
    left: 50px;
    top: 172px;
    width: 1100px;
    height: 626px;
    background: var(--card);
    border: 1.5px solid var(--card-edge);
  }
  .brand {
    position: absolute;
    left: 64px;
    top: 70px;
    display: flex;
    align-items: center;
    gap: 28px;
  }
  .brand-mark {
    width: 190px;
    height: 190px;
    background: var(--accent);
  }
  .brand-name {
    font-size: 76px;
    font-weight: 400;
    line-height: 0.95;
    color: var(--ink);
  }
  .holder {
    position: absolute;
    left: 65px;
    top: 340px;
    width: 960px;
    text-align: right;
  }
  .holder-name {
    font-size: 37px;
    font-weight: 600;
    color: var(--accent-deep);
    line-height: 1.1;
    padding-bottom: 4px;
  }
  .holder-rule {
    height: 2px;
    background: var(--accent);
  }
  .holder-role {
    font-size: 30px;
    font-weight: 400;
    line-height: 1.3;
    margin-top: 2px;
  }
  .contacts {
    position: absolute;
    left: 70px;
    top: 438px;
    list-style: none;
  }
  .contact {
    display: flex;
    align-items: center;
    gap: 12px;
    font-size: 24px;
    height: 34px;
    margin-bottom: 15px;
  }
  .contact svg { width: 16px; height: 20px; flex: none; }
  .services {
    position: absolute;
    left: 0;
    width: 100%;
    top: 560px;
    text-align: center;
    font-size: 27px;
    letter-spacing: 0.3px;
  }
</style>
</head>
<body>
  <main class="card">
    <div class="brand">
      <div class="brand-mark"></div>
      <div class="brand-name">Coralwood<br>Electrical</div>
    </div>

    <section class="holder">
      <h1 class="holder-name">Dominic Farrow</h1>
      <div class="holder-rule"></div>
      <p class="holder-role">Manager</p>
    </section>

    <ul class="contacts">
      <li class="contact">
        <svg viewBox="0 0 16 20" aria-hidden="true">
          <rect x="2" y="1" width="12" height="18" rx="2" fill="none" stroke="var(--accent)" stroke-width="2"/>
          <circle cx="8" cy="15.5" r="1.2" fill="var(--accent)"/>
        </svg>
        <span>0452 317 908</span>
      </li>
      <li class="contact">
        <svg viewBox="0 0 16 20" aria-hidden="true">
          <rect x="0.5" y="5" width="15" height="11" fill="var(--accent)"/>
          <path d="M0.5 5 L8 11 L15.5 5" fill="none" stroke="var(--card)" stroke-width="1.4"/>
        </svg>
        <span>dominic@coralwoodelectrical.com.au</span>
      </li>
    </ul>

    <p class="services">ELECTRICAL - COMMUNICATIONS - AUDIO - VISUAL</p>
  </main>
</body>
</html>
```